Packaging design for high end, natural skin care line needed

Marisol Thackery Beauty needs a label design. It is a new skin care line I am launching.
For years my line Velvet Orchard Beauty was quite popular and featured in several magazines, but for personal reasons had to be shut down. Now I am launching a new line featuring VOB's top selling products, but focused solely on skin care more so than cosmetics. All products will still be handmade, but the line should still look professional-something worthy of a Brindle Market shelf!
I am branding it with my name, as I am often quoted in articles related to gluten in beauty products, so Marisol Thackery and beauty are key words.
The key products will be facial and body serums which are packaged in .5oz., 1oz. and larger amber glass bottles with black dropper tops, I will include pictures below. For dimensions, the labels can be any size that you think will work best, but need to at the least fit the 1oz. bottle, dimensions shown here http://www.corvelflask.example/amber-glass-tall-round-flask/p/QZ7K-93/
I loved the former VOB logo, but for Marisol Thackery Beauty I am looking for something more personal, more apothecary-like, and probably less colorful.
The line will be small, just a handful of products, but luxe, rich.
I am attaching photos of Velvet Orchard Beauty's packaging for your reference.
Thanks much!!

Hi Everyone! Thank you for your submissions! Please see the links I provided in the brief, I really am looking for something more technical looking, like an apothecary. And want black text on a white background, not a black background, and nothing flowery.
Thank you all!!
Marisol

Target Market(s)

My clients are primarily women of all ages, but with more of a skin care focus, and no longer a cosmetic one, I would also like to appeal to a male audience. My clients are health conscious, gluten-free, natural, paleo, or vegan, etc. Target age is probably 25-55. Products are a bit high end, priced $45-65.

Industry/Entity Type

Cosmetics

Requirements
Must have
• It must at least say Marisol Thackery, or can say Marisol Thackery Beauty, but "Beauty" is not necessary. And capitalization is open, try whatever you think serves the brand. Likely slogans or taglines that can be included but are not essential: Care for your skin. Love and care for your skin. Handmade with love in the USA. Handmade in the USA. Think modern day apothecary. Small batch scotch. Something fine, but custom, handmade.
Nice to have
• I like the aesthetic of Oribel Skin Care a bit http://www.oribelhollis.example.au/
And of Dorian Valtz as shown here http://www.pinboardia.example/pin/847302915563017442/
Also of something like this that is even customizable http://www.pinboardia.example/pin/58274106392285514/
Every product is handmade in small batches, with fine ingredients, a moderate price point of around $45-$65. And I will likely begin making custom orders. So there could be a space to say when it was made, or for whom. I would like to keep the colors classic though, I probably want to stay away from the bright pink on this one.
Should not have
• As I mentioned, probably want to stay away from a lot of color. I like black vs. gray for the text, as it will show up better in editorials. I must look good, but also photograph well. Thanks!

```html
<!DOCTYPE html>
<html lang="en">
<head>
<meta charset="utf-8">
<title>Marisol Thackery – Body Serum Label</title>
<link rel="stylesheet" href="https://fonts.googleapis.com/css2?family=EB+Garamond:wght@400&display=swap">
<style>
  :root {
    --canvas: #ffffff;
    --label-paper: #ffffff;
    --ink: #111111;
    --rule: #111111;
    --shadow: rgba(0, 0, 0, 0.22);
  }
  * { margin: 0; padding: 0; box-sizing: border-box; }
  html, body {
    width: 1200px;
    height: 993px;
    overflow: hidden;
    background: var(--canvas);
  }
  .canvas {
    position: relative;
    width: 1200px;
    height: 993px;
    background: var(--canvas);
    font-family: "EB Garamond", "Times New Roman", serif;
    color: var(--ink);
  }
  .label {
    position: absolute;
    left: 197px;
    top: 261px;
    width: 248px;
    height: 326px;
    display: flex;
    background: var(--label-paper);
    border: 1px solid var(--rule);
    box-shadow: 2px 3px 6px var(--shadow);
  }
  .tagline-strip {
    width: 42px;
    height: 100%;
    position: relative;
    border-right: 1px solid var(--rule);
  }
  .tagline {
    position: absolute;
    left: 50%;
    top: 50%;
    transform: translate(-50%, -50%) rotate(-90deg);
    white-space: nowrap;
    font-size: 19.5px;
    font-weight: 400;
    letter-spacing: 0.5px;
    text-transform: uppercase;
    color: var(--ink);
  }
  .label-panel {
    flex: 1;
    height: 100%;
    position: relative;
    text-align: center;
  }
  .brand-name {
    position: absolute;
    left: 0;
    right: 0;
    top: 34px;
    font-size: 31px;
    line-height: 1.12;
    font-weight: 400;
    letter-spacing: 0.5px;
  }
  .product-name {
    position: absolute;
    left: 0;
    right: 0;
    top: 224px;
    font-size: 20px;
    font-weight: 400;
    letter-spacing: 0.3px;
  }
  .product-rule {
    position: absolute;
    left: 51px;
    top: 253px;
    width: 105px;
    height: 1px;
    background: var(--rule);
  }
  .volume {
    position: absolute;
    left: 0;
    right: 0;
    top: 290px;
    font-size: 16px;
    font-weight: 400;
    letter-spacing: 0.5px;
  }
</style>
</head>
<body>
  <main class="canvas">
    <section class="label" aria-label="Body serum label">
      <div class="tagline-strip">
        <p class="tagline">Love &amp; Care for Your Skin</p>
      </div>
      <div class="label-panel">
        <h1 class="brand-name">Marisol<br>Thackery</h1>
        <h2 class="product-name">BODY SERUM</h2>
        <div class="product-rule"></div>
        <p class="volume">5oz</p>
      </div>
    </section>
  </main>
</body>
</html>
```